Brom-leigh Sky Harbour Custom Brokers Limited

Shop online from the USA and Ship to Jamaica
Customs Brokerage, Import Export and logistic Services
Address:- 238-240 Halden Brook Road Kingston Jamaica
Email: info@bromleighskyharbour,com
Web: www.bromleighskyharbour.com
Telephone: (876) 555-0148, (876) 555-0193
flyer should be quarter page must print information on back and front

```html
<!DOCTYPE html>
<html lang="en">
<head>
<meta charset="utf-8">
<title>Brom-leigh Sky Harbour Custom Brokers – Quarter Page Flyer</title>
<link rel="stylesheet" href="https://fonts.googleapis.com/css2?family=Montserrat:wght@400;500;600;700&family=Comfortaa:wght@700&display=swap">
<style>
:root{
  --navy:#13305f;
  --navy-deep:#0d2550;
  --gold:#f0ad00;
  --white:#ffffff;
  --paper:#e9e9ea;
  --ink:#1c2b4a;
}
*{box-sizing:border-box;margin:0;padding:0}
html,body{width:1200px;height:602px;overflow:hidden;background:var(--paper);font-family:"Montserrat",sans-serif}
.sheet{position:relative;width:1200px;height:602px}
.card{position:absolute;top:80px;width:570px;height:442px;background:var(--white);overflow:hidden;box-shadow:0 4px 14px rgba(0,0,0,.18)}
.card--front{left:20px}
.card--back{left:610px}
.layer{position:absolute;left:0;top:0}
.photo{position:absolute;left:0;top:0;width:570px;height:300px;
  background:linear-gradient(100deg,#3b4f7e 0%,#9a5a55 22%,#d98a3c 45%,#f6c66a 58%,#e8a24c 72%,#6b7c99 100%)}
.brand{position:absolute;text-align:center;color:var(--navy)}
.brand__name{display:flex;align-items:center;justify-content:center;gap:6px;font-weight:700;font-size:14px;letter-spacing:.5px}
.brand__dot{width:12px;height:12px;border-radius:50%;background:var(--gold)}
.brand__sub{font-size:7px;letter-spacing:3px;color:#6b7892;margin-top:2px}
.card--front .brand{left:0;width:570px;top:62px}
.headline{font-family:"Comfortaa",sans-serif;font-weight:700;text-transform:uppercase;line-height:1.2}
.headline .gold{color:var(--gold)}
.headline .light{color:var(--white)}
.card--front .headline{position:absolute;left:0;top:112px;width:570px;height:56px;padding-top:6px;
  background:rgba(19,48,95,.62);text-align:center;font-size:20px}
.pill{position:absolute;background:var(--gold);color:var(--white);font-weight:600;font-size:11px;
  padding:3px 14px;border-radius:12px;transform:translateX(-50%);white-space:nowrap}
.about{position:absolute;left:30px;top:322px;width:510px;color:var(--white);font-size:8.3px;line-height:1.45;text-align:center}
.footer{position:absolute;left:0;bottom:0;width:570px;height:45px}
.footer__call{position:absolute;left:20px;top:11px;display:flex;align-items:center;gap:8px;color:var(--navy)}
.footer__call b{font-size:18px;font-weight:600;letter-spacing:.3px}
.footer__phones{font-size:8.5px;font-weight:600;line-height:1.45;color:var(--white)}
.footer__links{position:absolute;right:18px;top:15px;display:flex;gap:10px;font-size:8px;color:var(--ink)}
.footer__links span{display:flex;align-items:center;gap:4px}
.ico{width:11px;height:11px;border-radius:50%;background:var(--navy);display:inline-block;position:relative}
.ico svg{position:absolute;left:2px;top:2px}
.card--back .brand{left:0;width:290px;top:38px}
.card--back .headline{position:absolute;left:0;width:290px;top:110px;text-align:center;font-size:16.5px;line-height:1.3}
.card--back .headline .dark{color:var(--navy)}
.services{position:absolute;left:22px;top:240px;width:526px;height:128px;border:1px solid var(--gold)}
.services__row{position:absolute;left:0;top:14px;width:100%;display:flex;justify-content:space-around}
.service{width:96px;text-align:center}
.service__icon{width:30px;height:30px;margin:0 auto 5px;border-radius:50%;background:var(--gold);display:flex;align-items:center;justify-content:center}
.service__title{color:var(--gold);font-size:8.5px;font-weight:600;margin-bottom:2px}
.service__text{color:var(--white);font-size:7.3px;line-height:1.35}
.address{position:absolute;left:0;top:370px;width:570px;text-align:center;color:var(--white);font-size:8.5px;font-weight:500}
</style>
</head>
<body>
<main class="sheet">

  <!-- FRONT -->
  <section class="card card--front" aria-label="Flyer front">
    <div class="photo" role="img" aria-label="Port scene at sunset with stacked shipping containers, cargo ship, truck, plane and a woman shopping on a laptop"></div>

    <div class="brand">
      <div class="brand__name"><span class="brand__dot"></span>BROM-LEIGH SKY HARBOUR</div>
      <div class="brand__sub">Custom Brokers Ltd.</div>
    </div>

    <h1 class="headline"><span class="gold">Shop online from the USA</span><br><span class="light">And ship to Jamaica</span></h1>

    <svg class="layer" width="570" height="442" viewBox="0 0 570 442" aria-hidden="true">
      <path d="M0 232 C60 300 140 300 230 275 C330 246 420 215 570 245 L570 442 L0 442 Z" fill="var(--navy)"/>
      <path d="M0 232 C60 300 140 300 230 275 C330 246 420 215 570 245" fill="none" stroke="var(--gold)" stroke-width="5"/>
      <path d="M0 397 L570 397 L570 442 L0 442 Z" fill="var(--white)"/>
      <path d="M0 397 L240 397 L275 442 L0 442 Z" fill="var(--gold)"/>
    </svg>

    <span class="pill" style="left:285px;top:297px">ABOUT US</span>
    <p class="about">Sed ut perspiciatis unde omnis iste natus error sit voluptatem accusantium dol orem que laudantium, totam rem aperiam, eaque ipsa quae ab illo invent ore veritatis et quasi architecto beatae vitae dicta sunt explicabo. Nemo enim ipsam voluptatem quia volupt as sit aspernatur aut odit aut fugit, sed quia consequunt ur magni dolores eos qui ratione voluptatem sequi nesciunt. Neque porro quisquam est, qui dolorem ipsum quia dolor sit amet, consectetur, adipisci velit, sed quia non numquam eius modi tempora incidu nt ut labore et dolore magnam aliquam quaerat voluptatem.</p>

    <div class="footer">
      <div class="footer__call"><b>CALL US</b>
        <svg width="9" height="20" viewBox="0 0 9 20" aria-hidden="true"><path d="M2 1 L4 3 L3 5 Q4 7 6 8 L7 7 L9 9 L8 10 Q3 9 1 3 Z" fill="var(--navy)"/><path d="M2 11 L4 13 L3 15 Q4 17 6 18 L7 17 L9 19 L8 20 Q3 19 1 13 Z" fill="var(--navy)"/></svg>
        <div class="footer__phones">(876) 555-0148<br>(876) 555-0193</div>
      </div>
      <div class="footer__links">
        <span><i class="ico"><svg width="7" height="7" viewBox="0 0 7 7"><rect x="0" y="1" width="7" height="5" fill="#fff"/><path d="M0 1 L3.5 4 L7 1" stroke="var(--navy)" fill="none" stroke-width=".8"/></svg></i>info@bromleighskyharbour.com</span>
        <span><i class="ico"><svg width="7" height="7" viewBox="0 0 7 7"><circle cx="3.5" cy="3.5" r="3" fill="none" stroke="#fff" stroke-width=".8"/><path d="M0.5 3.5 H6.5 M3.5 0.5 V6.5" stroke="#fff" stroke-width=".7"/></svg></i>www.bromleighskyharbour.com</span>
      </div>
    </div>
  </section>

  <!-- BACK -->
  <section class="card card--back" aria-label="Flyer back">
    <svg class="layer" width="570" height="442" viewBox="0 0 570 442">
      <defs>
        <linearGradient id="backPhoto" x1="0" y1="0" x2="1" y2="1">
          <stop offset="0" stop-color="#3f5f8c"/>
          <stop offset=".45" stop-color="#f3c46a"/>
          <stop offset=".7" stop-color="#d9822f"/>
          <stop offset="1" stop-color="#505f78"/>
        </linearGradient>
      </defs>
      <path role="img" aria-label="Container terminal with cranes, yellow truck, cargo ship and plane at sunrise"
        d="M258 0 L570 0 L570 178 C500 200 420 200 360 180 C290 155 250 95 258 0 Z" fill="url(#backPhoto)"/>
      <path d="M258 0 C250 95 290 155 360 180 C420 200 500 200 570 178" fill="none" stroke="var(--gold)" stroke-width="5"/>
      <path d="M0 225 C120 195 260 215 380 212 C460 210 520 200 570 190 L570 442 L0 442 Z" fill="var(--navy)"/>
      <path d="M0 222 C120 192 260 212 380 209 C460 207 520 197 570 187" fill="none" stroke="var(--gold)" stroke-width="4"/>
      <path d="M0 397 L570 397 L570 442 L0 442 Z" fill="var(--white)"/>
      <path d="M0 397 L240 397 L275 442 L0 442 Z" fill="var(--gold)"/>
    </svg>

    <div class="brand">
      <div class="brand__name"><span class="brand__dot"></span>BROM-LEIGH SKY HARBOUR</div>
      <div class="brand__sub">Custom Brokers Ltd.</div>
    </div>

    <h2 class="headline"><span class="gold">Shop online<br>from the USA</span><br><span class="dark">And ship to Jamaica</span></h2>

    <div class="services">
      <div class="services__row">
        <div class="service">
          <div class="service__icon"><svg width="18" height="12" viewBox="0 0 18 12"><rect x="1" y="1" width="10" height="7" fill="none" stroke="var(--navy)" stroke-width="1.2"/><path d="M11 3 H15 L17 6 V8 H11 Z" fill="none" stroke="var(--navy)" stroke-width="1.2"/><circle cx="4" cy="10" r="1.5" fill="var(--navy)"/><circle cx="14" cy="10" r="1.5" fill="var(--navy)"/></svg></div>
          <div class="service__title">SHIPPING</div>
          <div class="service__text">Sed ut perspiciatis unde omnis iste natus error</div>
        </div>
        <div class="service">
          <div class="service__icon"><svg width="16" height="14" viewBox="0 0 16 14"><rect x="1" y="3" width="6" height="7" fill="none" stroke="var(--navy)" stroke-width="1.2"/><path d="M7 1 V11 H15" fill="none" stroke="var(--navy)" stroke-width="1.2"/><rect x="9" y="5" width="5" height="5" fill="var(--navy)"/><circle cx="3" cy="12" r="1.4" fill="var(--navy)"/></svg></div>
          <div class="service__title">LOGISTICS</div>
          <div class="service__text">Sed ut perspiciatis unde omnis iste natus error</div>
        </div>
        <div class="service">
          <div class="service__icon"><svg width="13" height="15" viewBox="0 0 13 15"><rect x="1" y="1" width="11" height="13" fill="none" stroke="var(--navy)" stroke-width="1.2"/><path d="M3 5 H10 M3 8 H10 M3 11 H7" stroke="var(--navy)" stroke-width="1.1"/></svg></div>
          <div class="service__title">CUSTOM CLEARENCE</div>
          <div class="service__text">Sed ut perspiciatis unde omnis iste natus error</div>
        </div>
        <div class="service">
          <div class="service__icon"><svg width="16" height="16" viewBox="0 0 16 16"><path d="M8 1 L9 6 L15 9 V10.5 L9 9 L8.8 13 L10.5 14.5 V15.5 L8 15 L5.5 15.5 V14.5 L7.2 13 L7 9 L1 10.5 V9 L7 6 Z" fill="var(--navy)"/></svg></div>
          <div class="service__title">EXPORT</div>
          <div class="service__text">Sed ut perspiciatis unde omnis iste natus error</div>
        </div>
        <div class="service">
          <div class="service__icon"><svg width="16" height="15" viewBox="0 0 16 15"><path d="M2 6 L8 9 L14 6 V12 L8 14.5 L2 12 Z" fill="none" stroke="var(--navy)" stroke-width="1.2"/><path d="M8 0.5 V6 M5.5 3.5 L8 6 L10.5 3.5" fill="none" stroke="var(--navy)" stroke-width="1.2"/></svg></div>
          <div class="service__title">IMPORTS</div>
          <div class="service__text">Sed ut perspiciatis unde omnis iste natus error</div>
        </div>
      </div>
    </div>
    <span class="pill" style="left:285px;top:231px">OUR SERVICES</span>

    <p class="address"><svg width="7" height="10" viewBox="0 0 7 10" aria-hidden="true" style="vertical-align:-1px;margin-right:4px"><path d="M3.5 10 L0.7 5 A3.2 3.2 0 1 1 6.3 5 Z" fill="var(--gold)"/><circle cx="3.5" cy="3.5" r="1.2" fill="var(--navy)"/></svg>238-240 Halden Brook Road Kingston Jamaica</p>

    <div class="footer">
      <div class="footer__call"><b>CALL US</b>
        <svg width="9" height="20" viewBox="0 0 9 20" aria-hidden="true"><path d="M2 1 L4 3 L3 5 Q4 7 6 8 L7 7 L9 9 L8 10 Q3 9 1 3 Z" fill="var(--navy)"/><path d="M2 11 L4 13 L3 15 Q4 17 6 18 L7 17 L9 19 L8 20 Q3 19 1 13 Z" fill="var(--navy)"/></svg>
        <div class="footer__phones">(876) 555-0148<br>(876) 555-0193</div>
      </div>
      <div class="footer__links">
        <span><i class="ico"><svg width="7" height="7" viewBox="0 0 7 7"><rect x="0" y="1" width="7" height="5" fill="#fff"/><path d="M0 1 L3.5 4 L7 1" stroke="var(--navy)" fill="none" stroke-width=".8"/></svg></i>info@bromleighskyharbour.com</span>
        <span><i class="ico"><svg width="7" height="7" viewBox="0 0 7 7"><circle cx="3.5" cy="3.5" r="3" fill="none" stroke="#fff" stroke-width=".8"/><path d="M0.5 3.5 H6.5 M3.5 0.5 V6.5" stroke="#fff" stroke-width=".7"/></svg></i>www.bromleighskyharbour.com</span>
      </div>
    </div>
  </section>

</main>
</body>
</html>
```